Clean and Polished Store Design

Please design a website similar to this one: http://veltrasign.com/
We require two pages:
* the home page: http://veltrasign.com/
* the product page: http://veltrasign.com/products/our-printer
Notice that there are few words and more pictures. It's clean and professional. Although I think their product page is difficult to read because it is too spread out.
Please help us generate excitement for our product via a polished and high-end looking web design. Please keep it VERY SIMPLE.
Target Market(s)
Our target market is consumers that have never bought a 3D printer before and those to whom 3D printing is new but exciting. Our market is not very technical. They love the sleek look of the printer and its ease of use.
Industry/Entity Type
Printer
Requirements
Must have
- We require two pages:
- * the home page: http://veltrasign.com/
- * the product page: http://veltrasign.com/products/our-printer
- One of our product renderings must be displayed on both the homepage and the product page.
- Our logo must be displayed on both pages.
- The pages must have a header, a footer and content equivalent to the veltrasign website.

```html
<!DOCTYPE html>
<html lang="en">
<head>
<meta charset="utf-8">
<title>Stratum – High Resolution Desktop 3D Printer</title>
<link rel="stylesheet" href="https://fonts.googleapis.com/css2?family=Roboto+Condensed:wght@300;400;700&family=Arimo:wght@400;700&display=swap">
<style>
  :root {
    --ink: #111111;
    --heading: #666666;
    --body: #555555;
    --rule: #d6d6d6;
    --slide-bg: #e8e8e8;
    --accent: #ff8000;
    --footer-bg: #161616;
    --footer-text: #e6e6e6;
    --social: #7a7a7a;
    --white: #ffffff;
  }
  * { margin: 0; padding: 0; box-sizing: border-box; }
  html, body { width: 1200px; height: 960px; overflow: hidden; background: var(--white); }
  body { position: relative; font-family: "Arimo", Arial, sans-serif; color: var(--body); }

  .top-band { position: absolute; left: 0; top: 0; width: 1200px; height: 5px; background: var(--ink); }

  .site-header { position: absolute; left: 130px; top: 5px; width: 960px; height: 128px; border-bottom: 1px solid var(--rule); }
  .brand { position: absolute; left: 0; top: 42px; text-decoration: none; }
  .brand-name { font-family: "Roboto Condensed", sans-serif; font-weight: 400; font-size: 40px; line-height: 1; color: var(--ink); letter-spacing: 2px; }

  .main-nav { position: absolute; right: 0; top: 48px; display: flex; align-items: center; }
  .main-nav a { font-family: "Roboto Condensed", sans-serif; font-size: 15px; color: var(--ink); text-decoration: none; margin-right: 38px; }
  .main-nav a:nth-child(4) { margin-right: 22px; }
  .cart { display: flex; align-items: center; gap: 12px; width: 80px; height: 36px; border: 1px solid var(--rule); padding-left: 9px; font-family: "Roboto Condensed", sans-serif; font-size: 17px; color: var(--ink); }

  .hero-slider { position: absolute; left: 128px; top: 207px; width: 412px; height: 391px; border: 1px solid #cfcfcf; box-shadow: 0 0 2px rgba(0,0,0,.15); background: var(--slide-bg); }
  .hero-render { position: absolute; left: 80px; top: 75px; width: 252px; height: 250px; border-radius: 30px;
    background: radial-gradient(circle at 45% 40%, #ffb060 0%, #ff8a1c 45%, #e86a00 75%, rgba(232,106,0,0) 100%); }
  .slider-dots { position: absolute; left: 187px; top: 372px; display: flex; gap: 6px; }
  .slider-dots span { width: 8px; height: 8px; border-radius: 50%; background: #b5b5b5; }
  .slider-dots span.is-active { background: var(--ink); }

  .hero-copy { position: absolute; left: 615px; top: 278px; width: 475px; }
  .hero-title { font-family: "Roboto Condensed", sans-serif; font-weight: 300; font-size: 60px; line-height: 64px; color: var(--heading); }
  .hero-subtitle { font-family: "Roboto Condensed", sans-serif; font-weight: 300; font-size: 24px; line-height: 29px; color: var(--heading); margin-top: -3px; }
  .hero-text { font-size: 12px; line-height: 17px; color: var(--body); text-align: justify; margin-top: 17px; }
  .order-button { display: inline-block; margin-top: 13px; margin-left: 2px; width: 140px; height: 45px; border-radius: 23px; border: 1px solid #c9c9c9;
    background: linear-gradient(#ffffff, #e4e4e4); font-family: "Roboto Condensed", sans-serif; font-weight: 300; font-size: 20px; line-height: 43px;
    text-align: center; color: #8a8a8a; text-decoration: none; }

  .feature { position: absolute; top: 655px; width: 460px; }
  .feature--output { left: 129px; }
  .feature--easy { left: 630px; }
  .feature-title { font-family: "Roboto Condensed", sans-serif; font-weight: 300; font-size: 22px; line-height: 26px; color: var(--heading); }
  .feature-lead { font-size: 12px; line-height: 18px; color: var(--accent); margin-top: 14px; letter-spacing: -0.25px; width: 465px; }
  .feature-text { font-size: 12px; line-height: 18px; color: var(--body); text-align: justify; margin-top: 18px; }

  .site-footer { position: absolute; left: 0; top: 870px; width: 1200px; height: 90px; background: var(--footer-bg); }
  .legal { position: absolute; left: 129px; top: 28px; font-family: "Roboto Condensed", sans-serif; font-weight: 300; font-size: 12px; color: var(--footer-text); }
  .legal a { color: var(--footer-text); text-decoration: none; }
  .social { position: absolute; left: 1000px; top: 25px; display: flex; gap: 3px; }
  .social span { width: 20px; height: 20px; border-radius: 50%; background: var(--social); }
</style>
</head>
<body>
  <div class="top-band"></div>

  <header class="site-header">
    <a class="brand" href="#"><span class="brand-name">STRATUM</span></a>
    <nav class="main-nav">
      <a href="#">ABOUT</a>
      <a href="#">SUPPORT</a>
      <a href="#">STORE</a>
      <a href="#">LOGIN</a>
      <span class="cart">
        <svg width="28" height="20" viewBox="0 0 28 20" aria-hidden="true">
          <path d="M1 2h5l3 11h14l3-8H8" fill="none" stroke="#111" stroke-width="2"/>
          <circle cx="11" cy="17" r="2" fill="#111"/><circle cx="21" cy="17" r="2" fill="#111"/>
        </svg>
        : 0
      </span>
    </nav>
  </header>

  <section class="hero-slider">
    <div class="hero-render" role="img" aria-label="Orange rounded-cube desktop 3D printer rendering"></div>
    <div class="slider-dots"><span class="is-active"></span><span></span><span></span></div>
  </section>

  <section class="hero-copy">
    <h1 class="hero-title">STRATUM 3D</h1>
    <p class="hero-subtitle">High Resolution<br>Desktop 3D Printer</p>
    <p class="hero-text">consectetur adipisicing elit, sed do eiusmod tempor incididunt ut labore et dolore magna aliqua. Ut enim ad minim veniam, quis nostrud exercitation ullamco laboris consectetur adipisicing elit, sed do eiusmod tempor incididunt ut labore et dolore magna aliqua. Ut enim ad minim veniam, quis nostrud exercitation ullamco laboris</p>
    <a class="order-button" href="#">ORDER NOW!</a>
  </section>

  <section class="feature feature--output">
    <h2 class="feature-title">PROFESSIONAL OUTPUT</h2>
    <p class="feature-lead">Sed ut perspiciatis unde omnis iste natus error sit voluptatem accusantium doloremque laudantium, totam rem aperiam,</p>
    <p class="feature-text">Nemo enim ipsam voluptatem quia voluptas sit aspernatur aut odit aut fugit, sed quia consequuntur magni dolores eos qui ratione voluptatem sequi nesciunt. Neque porro quisquam est, qui dolorem ipsum quia dolor sit amet, consectetur, adipisci velit, sed quia non numquam eius modi tempora incidunt ut labore et dolore magnam aliquam quaerat voluptatem.</p>
  </section>

  <section class="feature feature--easy">
    <h2 class="feature-title">ACCESSIBLE AND EASY ›</h2>
    <p class="feature-lead">Sed ut perspiciatis unde omnis iste natus error sit voluptatem accusantium doloremque laudantium, totam rem aperiam,</p>
    <p class="feature-text">Nemo enim ipsam voluptatem quia voluptas sit aspernatur aut odit aut fugit, sed quia consequuntur magni dolores eos qui ratione voluptatem sequi nesciunt. Neque porro quisquam est, qui dolorem ipsum quia dolor sit amet, consectetur, adipisci velit, sed quia non numquam eius modi tempora incidunt ut labore et dolore magnam aliquam quaerat voluptatem.</p>
  </section>

  <footer class="site-footer">
    <p class="legal">© STRATUM 2012 - <a href="#">PRIVACY POLICY</a> - <a href="#">TERMS OF SERVICE</a></p>
    <div class="social" aria-label="Social links"><span></span><span></span><span></span><span></span></div>
  </footer>
</body>
</html>
```